Eco-friendly printer cartridges and toners packaging

Dear designers,

we are looking for a new packaging design for remanufactured printer consumables products. The design should clearly communicate ecology and economy (check inspirations attached - we like them :) ). To understand the ecological impact you can watch the presentation at http://www.verdalink.sk/ecology.html . You can find also more information about the brand at http://www.verdalink.sk/index1.html .

We currently need universal design for following sizes of product:

cartridges:

1. 60x25x90 mm
2. 60x45x90 mm
3. 80x45x120 mm

laser toners:

4. 178x110x345 mm

They all should be recoginezed at the first sight, that it is the same brand and by buying this product the customer contributes to saving enviroment and supports socially responsible company, while it also saves his/hers money.

The final packaging will be in blister.

And be as creative as possible. Its all up to you.

Feel free to ask as many questions as needed.

You do not have to stick to the packaging design and sizes in the attachement. The only thing you need to stick to is the actual product measures.
Updates

Project Deadline Extended
Reason: As we have a little more time than we expected, we postpone the deadline. We also have a lot of accepted project invitations and we are expecting the delivery. Thank you for understanding. Marek

Target Market(s)

Anyone who buys printer consumables. It should attract everyone who thinks ecologically and wants to save some money

Industry/Entity Type

It Company

Requirements
Must have
• 1. logo - will be attached (if you dont like current logo you can try to design new one)
2. ecological messages - up to you
3. Slovak and English manual - will be attached
4. Pictograms - will be attached (can be redisigned)
5. Compatibility - which printers is the cartridge/toner compatible with (blank space to be filled in)
6. Slovak and English copyright disclaimer - will be attached
7. Colour identification (black, cyan, magenta....)
8. ISO 9001 / ISO 14001
9. Made in Europe
10. Production Date
11. Part no.
12. Use before text - will be attached
Nice to have
• 1.we are currently remanufacturing cartridges and toners for printers of 12 different brands (vortana, qz, belvix, miralt...) The packaging should be somehow differentiated for each different brand (either by colour / it can be different colour of some line, or the whole backgroud or just some spot on the packaging/, different fruit on the packaging, or whatever you consider to be the best option.

2. nature in the design

```html
<!DOCTYPE html>
<html lang="en">
<head>
<meta charset="utf-8">
<title>Vireno – Remanufactured Cartridge Packaging</title>
<link rel="stylesheet" href="https://fonts.googleapis.com/css2?family=Dosis:wght@500;600&display=swap">
<style>
  :root {
    --canvas-bg: #eef1ee;
    --brand-green: #00944a;
    --text-green: #12a150;
    --micro-green: #2bb45f;
    --leaf-deep: #1e9d45;
    --leaf-mid: #5cc46c;
    --leaf-light: #b9e3b6;
    --panel-white: #ffffff;
    --side-white: #f7f8f7;
    --edge: #dfe3df;
  }
  * { margin: 0; padding: 0; box-sizing: border-box; }
  html, body {
    width: 1200px; height: 900px; overflow: hidden;
    background: var(--canvas-bg);
    font-family: "Dosis", "Arial Narrow", sans-serif;
  }
  .canvas { position: relative; width: 1200px; height: 900px; }

  .package { position: absolute; box-shadow: 0 14px 30px rgba(0,0,0,.08); }
  .package--small { left: 140px; top: 250px; width: 400px; height: 550px; }
  .package--large { left: 612px; top: 105px; width: 393px; height: 695px; }

  .hang-tab { position: absolute; left: 0; top: 0; width: 100%; background: var(--brand-green); }
  .package--small .hang-tab { height: 95px; }
  .package--large .hang-tab { height: 140px; }
  .hang-hole { position: absolute; background: var(--canvas-bg); border-radius: 48% 48% 18% 18% / 70% 70% 30% 30%; }
  .package--small .hang-hole { left: 95px; top: 28px; width: 140px; height: 55px; }
  .package--large .hang-hole { left: 92px; top: 58px; width: 150px; height: 60px; }

  .top-flap {
    position: absolute; left: 0; width: 100%; height: 30px;
    background: var(--side-white); border-bottom: 1px solid var(--edge);
    padding: 8px 14px; color: var(--micro-green);
    font-size: 7px; line-height: 8px; letter-spacing: .3px; text-transform: uppercase;
    white-space: nowrap; overflow: hidden;
  }
  .package--small .top-flap { top: 95px; }
  .package--large .top-flap { top: 140px; height: 35px; }

  .side-panel {
    position: absolute; left: 0; bottom: 0; width: 62px;
    background: var(--side-white); border-right: 1px solid var(--edge);
    padding: 10px 6px; color: var(--micro-green);
    font-size: 6px; line-height: 7px; text-transform: uppercase; letter-spacing: .2px;
  }
  .package--small .side-panel { top: 125px; }
  .package--large .side-panel { top: 175px; }
  .micro-copy p { margin-bottom: 1px; }
  .pictograms { display: block; margin: 14px 0 10px; }
  .label-field {
    position: absolute; left: 6px; right: 6px; bottom: 12px; height: 40px;
    border: 1px solid var(--edge); background: var(--panel-white);
  }

  .front-panel {
    position: absolute; left: 62px; right: 0; bottom: 0;
    background: var(--panel-white); overflow: hidden;
  }
  .package--small .front-panel { top: 125px; }
  .package--large .front-panel { top: 175px; }

  .wordmark {
    position: absolute; color: var(--text-green);
    font-weight: 600; letter-spacing: 1px; line-height: 1; white-space: nowrap;
  }
  .package--small .wordmark { right: 24px; top: 16px; font-size: 40px; }
  .package--large .wordmark { right: 22px; top: 106px; font-size: 40px; }

  .leaf-artwork { position: absolute; }
  .package--small .leaf-artwork {
    left: 0; top: 20px; width: 320px; height: 400px;
    background:
      radial-gradient(ellipse 40% 30% at 30% 70%, var(--leaf-deep) 0%, rgba(30,157,69,0) 100%),
      radial-gradient(ellipse 45% 35% at 25% 30%, var(--leaf-mid) 0%, rgba(92,196,108,0) 100%),
      radial-gradient(ellipse 50% 45% at 65% 55%, var(--leaf-light) 0%, rgba(185,227,182,0) 100%);
  }
  .package--large .leaf-artwork {
    left: 0; top: 160px; width: 330px; height: 460px;
    background:
      radial-gradient(ellipse 35% 45% at 30% 55%, var(--leaf-mid) 0%, rgba(92,196,108,0) 100%),
      radial-gradient(ellipse 40% 25% at 55% 25%, var(--leaf-light) 0%, rgba(185,227,182,0) 100%),
      radial-gradient(ellipse 25% 30% at 45% 80%, var(--leaf-deep) 0%, rgba(30,157,69,0) 100%);
  }
</style>
</head>
<body>
<main class="canvas">

  <section class="package package--small">
    <div class="hang-tab"><span class="hang-hole"></span></div>
    <div class="top-flap">Remanufactured ink cartridge · Made in Europe</div>
    <aside class="side-panel">
      <div class="micro-copy">
        <p>Quality tested refill</p>
        <p>Saves money and nature</p>
        <p>Recycled carton box</p>
        <p>ISO 9001 ISO 14001</p>
        <p>Use before date</p>
      </div>
      <svg class="pictograms" width="48" height="60" viewBox="0 0 48 60" fill="none" stroke="#2bb45f" stroke-width="1">
        <rect x="1" y="1" width="12" height="12"/><path d="M5 4v6M9 4v6"/>
        <rect x="18" y="1" width="12" height="12"/><path d="M21 4l3 6 3-6"/>
        <rect x="35" y="1" width="12" height="12"/><path d="M38 5h6M38 8h6"/>
        <rect x="1" y="16" width="12" height="12"/><circle cx="7" cy="22" r="3"/>
        <rect x="18" y="16" width="12" height="12"/><path d="M21 25h6M24 19v6"/>
        <rect x="35" y="16" width="12" height="12"/><path d="M38 25l3-6 3 6z"/>
        <rect x="1" y="31" width="12" height="12"/><path d="M4 37h6M7 34v6"/>
        <rect x="18" y="31" width="12" height="12"/><path d="M21 34h6v6h-6z"/>
        <rect x="35" y="31" width="12" height="12"/><path d="M41 34v6M38 37h6"/>
        <rect x="1" y="46" width="12" height="12"/><path d="M4 52l3 3 3-6"/>
        <rect x="18" y="46" width="12" height="12"/><circle cx="24" cy="52" r="2"/>
        <rect x="35" y="46" width="12" height="12"/><path d="M38 49l6 6M44 49l-6 6"/>
      </svg>
      <div class="micro-copy">
        <p>Part no colour black</p>
        <p>Production date</p>
      </div>
      <div class="label-field"></div>
    </aside>
    <div class="front-panel">
      <div class="leaf-artwork" role="img" aria-label="Illustration of fresh green leaves with water drops and light sparkles"></div>
      <h1 class="wordmark">VIRENO</h1>
    </div>
  </section>

  <section class="package package--large">
    <div class="hang-tab"><span class="hang-hole"></span></div>
    <div class="top-flap">Remanufactured ink cartridge · Made in Europe</div>
    <aside class="side-panel">
      <div class="micro-copy">
        <p>Quality tested refill</p>
        <p>Saves money and nature</p>
        <p>Recycled carton box</p>
        <p>ISO 9001 ISO 14001</p>
        <p>Use before date</p>
      </div>
      <svg class="pictograms" width="48" height="60" viewBox="0 0 48 60" fill="none" stroke="#2bb45f" stroke-width="1">
        <rect x="1" y="1" width="12" height="12"/><path d="M5 4v6M9 4v6"/>
        <rect x="18" y="1" width="12" height="12"/><path d="M21 4l3 6 3-6"/>
        <rect x="35" y="1" width="12" height="12"/><path d="M38 5h6M38 8h6"/>
        <rect x="1" y="16" width="12" height="12"/><circle cx="7" cy="22" r="3"/>
        <rect x="18" y="16" width="12" height="12"/><path d="M21 25h6M24 19v6"/>
        <rect x="35" y="16" width="12" height="12"/><path d="M38 25l3-6 3 6z"/>
        <rect x="1" y="31" width="12" height="12"/><path d="M4 37h6M7 34v6"/>
        <rect x="18" y="31" width="12" height="12"/><path d="M21 34h6v6h-6z"/>
        <rect x="35" y="31" width="12" height="12"/><path d="M41 34v6M38 37h6"/>
        <rect x="1" y="46" width="12" height="12"/><path d="M4 52l3 3 3-6"/>
        <rect x="18" y="46" width="12" height="12"/><circle cx="24" cy="52" r="2"/>
        <rect x="35" y="46" width="12" height="12"/><path d="M38 49l6 6M44 49l-6 6"/>
      </svg>
      <div class="micro-copy">
        <p>Part no colour black</p>
        <p>Production date</p>
      </div>
      <div class="label-field"></div>
    </aside>
    <div class="front-panel">
      <div class="leaf-artwork" role="img" aria-label="Illustration of a green tea branch with long serrated leaves and a water drop"></div>
      <h1 class="wordmark">VIRENO</h1>
    </div>
  </section>

</main>
</body>
</html>
```